Hollow Lantern Town Strolling Past Tour

We are launching a different kind of city historical walking tour company with a slightly darker approach using historical but real stories that have long been forgotten from living memory.
Our tour is going to contain a lot of very thoroughly researched stories ranging from 50 to 150 years past that takes the customer into the actual-real life past of the city streets.  Stories that may contains some dark undertones and stories with a twist or that seem eccentric to us now but were entirely normal back in olden times - minus the dry historical facts that most tours engage in..
Our tours are going to run both day and night and will incorporate real history / real Hollow Lantern, so some of the stories will be quite serious (e.g.- there are actual murders from 100 years ago, baffling court cases, even a bit of poetry written by murderers, suicides, love triangles, you name it.  We are aiming for a mystery/history theme and are aiming to attract tourists who are interested in getting a different kind of history.

We're not going for scares and even though we expect people to enjoy our tours;  we're not aiming at light fun and frivolity.  I guess if you wanted to give us a tv rating we'd be aiming at M to MA15+.
If I was to give you another analogy using the literature world.  Think Edwin Harrowgates Nightwarden rather than the Moonveil Saga of movies.  Or Agnes Pellowe's Corvanthus rather than the Grimbles.  Even Crown of Embers rather than a soap opera.
Our stories are being carefully crafted and are packed with unexpected twists, turns & revelations whilst remaining all 100% true.  We have approx 15-20 stories for each tour and we're designing them in a way that each story will trigger a different range of emotions in the listeners on a regular basis.  We're being very careful to keep it fresh for each story so that it will next to impossible for our guests to zone out!  I personally can't stand going on a tour where mildly interesting facts are read out.  We like deep, rich stories rather than pop entertainment.
We want the website to generate a feeling/atmosphere for our product that draws the right crowd to our tours as well as making it easy to make a booking.  Basic features to include:-
Home Page
Bookings Page
Integration with a booking system will be required here via use of plugin code.
Private Functions Page
We are hoping to integrate with a booking system via use of plugin code.  If not, then a simple form enquiry type input e.g.- name, emails, subject, contact, details, preferred date/time, etc).
About Us Page :-
Dark; a euphemism for the unknown or the forgotten.  Think dark ages, dark matter, dark energy; things where knowledge is uncertain or unknown are often termed dark.   Hollow Lantern brings back the hidden past, the forgotten past, the past that may not want to be remembered……but these are real stories....real stories that come from the streets around you.

Some of these stories may be tales of dark things.....some may simply be a charming reminder of days gone by…..regardless these stories are compelling reminders of the amazing times that precede us…..and the forgotten people of yesteryear finally get a chance to have their story told to a fresh audience.  Through you, the people of yesterday get to live again.  Will you like what you hear?

Contact Us page:-
•	A form input type page.
•	Include space for our phone number
•	Include space for our email address
Other Items:-
Social Media Links; we will be looking for social media icons to link to our social media pages to Friendloop, Snapvista, Chirpline.
Subscription; we want to also capture an input email address box for site visitors.  We will be launching a weekly Hollow Lantern podcast / email newsetter; with a weekly Hollow Lantern from a different place in the world and we want some way for people to subscribe.

Updates
Project Deadline Extended
Reason: A few additional photos have been uploaded.  Feel free to utilize if helpful.  Our stories range from the 1800s to 1950s in an era with beautiful old Victorian buildings.  I'm putting through the extension just to give some more time to see if this gives any more ideas and inspiration.  Thank you for all the great submissions.

Target Market(s)
Tourists that want to hear a darker version of the city they are visiting. Stories that other tour companies would not even think of covering. The real history of the events that ordinary people lived through that didn't necessarily make the history books. All stories are true; as per project description.
Industry/Entity Type
Tourism
Coding
Coded - Design and coding required
Number of Pages Required
5+ page
Colors
Designer to choose colors to be used in the design.
Look and feel

```html
<!DOCTYPE html>
<html lang="en">
<head>
<meta charset="utf-8">
<title>Hollow Lantern — Town Strolling Past Tour</title>
<link href="https://fonts.googleapis.com/css2?family=Open+Sans:wght@400;600;700&family=Noto+Serif:wght@400;700&display=swap" rel="stylesheet">
<style>
  :root{
    --page:#ffffff;
    --ink:#2b2b2b;
    --muted:#7a7a7a;
    --line:#dcdcdc;
    --nav-top:#3a3532;
    --nav-bottom:#8a817b;
    --accent:#d8333a;
    --sky:#4f86c9;
    --stone:#b35a34;
    --band:#f3f1ef;
  }
  *{box-sizing:border-box;margin:0;padding:0}
  html,body{width:1200px;height:1200px;overflow:hidden;background:var(--page);font-family:"Open Sans",Arial,sans-serif;color:var(--ink)}
  .site{width:1200px;height:1200px;position:relative}

  .site-header{height:90px;display:flex;align-items:center;padding:0 40px;border-bottom:1px solid var(--line)}
  .brand{display:flex;align-items:center;gap:10px;font-size:20px;font-weight:700;color:var(--ink);letter-spacing:.5px;text-transform:uppercase}
  .brand-mark{width:18px;height:18px;background:var(--accent);border-radius:50%}
  .support{margin-left:auto;display:flex;align-items:center;gap:10px;font-size:12px;color:var(--muted);line-height:1.4}
  .support-icon{width:32px;height:32px;border-radius:50%;background:#222;display:flex;align-items:center;justify-content:center}
  .search{margin-left:28px;width:250px;height:36px;border:1px solid var(--line);border-radius:18px;display:flex;align-items:center;justify-content:space-between;padding:0 14px;font-size:12px;color:#9a9a9a}
  .login{margin-left:120px;font-size:15px;color:#555;display:flex;align-items:center;gap:5px;align-self:flex-start;margin-top:18px}

  .main-nav{height:38px;background:linear-gradient(180deg,var(--nav-top),var(--nav-bottom));display:flex;align-items:center;padding:0 40px;gap:22px}
  .main-nav a{color:#fff;font-size:12px;font-weight:700;text-decoration:none;text-transform:uppercase;letter-spacing:-.2px;white-space:nowrap}

  .hero{position:relative;height:620px;background:linear-gradient(180deg,var(--sky) 0%,#8fb4de 30%,var(--stone) 48%,#a24a2a 80%,#c9a888 100%)}
  .booking-panel{position:absolute;left:60px;right:60px;top:480px;height:150px;background:#fff;box-shadow:0 4px 16px rgba(0,0,0,.18);display:grid;grid-template-columns:1.15fr 1.15fr 1fr 1fr;padding:18px 22px 0}
  .step{padding:0 14px;border-right:1px solid var(--line)}
  .step:last-child{border-right:0}
  .step h3{font-size:14px;font-weight:400;margin-bottom:14px}
  .step h3 b{font-weight:700}
  .options{display:grid;grid-template-columns:1fr 1fr;gap:8px 10px;font-size:12px;color:#555}
  .opt{display:flex;align-items:center;gap:7px;white-space:nowrap}
  .radio{width:12px;height:12px;flex:none;border:1px solid #bbb;border-radius:50%}
  .radio.on{background:radial-gradient(circle,#888 35%,transparent 40%)}
  .label{font-size:12px;color:#555;margin-bottom:6px;white-space:nowrap}
  .field{height:28px;border:1px solid var(--line);border-radius:3px;font-size:11px;color:#aaa;padding:6px 8px;white-space:nowrap;overflow:hidden}
  .pair{display:grid;gap:8px}
  .pair.two{grid-template-columns:1fr 1fr}
  .pair.three{grid-template-columns:1fr 1fr 1fr}
  .proceed{position:absolute;left:50%;bottom:-14px;transform:translateX(-50%);background:var(--accent);color:#fff;font-size:11px;font-weight:700;text-transform:uppercase;padding:7px 34px;border-radius:3px;white-space:nowrap}

  .offers{background:var(--band);height:452px;padding:80px 60px 0}
  .offers h2{font-family:"Noto Serif",Georgia,serif;font-size:22px;font-weight:400;margin-bottom:26px}
  .offer-grid{display:grid;grid-template-columns:repeat(4,1fr);gap:10px}
  .offer{height:200px}
  .o1{background:linear-gradient(160deg,#c9b48a,#8a6e44)}
  .o2{background:linear-gradient(160deg,#9ab8d8,#b65a3c)}
  .o3{background:linear-gradient(160deg,#3c72c0,#a88b63)}
  .o4{background:linear-gradient(160deg,#c4a070,#8c5a34)}
</style>
</head>
<body>
<div class="site">
  <header class="site-header">
    <div class="brand"><span class="brand-mark"></span>Hollow Lantern</div>
    <div class="support">
      <span class="support-icon"><svg width="16" height="16" viewBox="0 0 24 24"><path fill="#d8333a" d="M6.6 10.8a15 15 0 0 0 6.6 6.6l2.2-2.2c.3-.3.7-.4 1-.2 1.1.4 2.3.6 3.6.6.6 0 1 .4 1 1V20c0 .6-.4 1-1 1A17 17 0 0 1 3 4c0-.6.4-1 1-1h3.5c.6 0 1 .4 1 1 0 1.3.2 2.5.6 3.6.1.3 0 .7-.2 1z"/></svg></span>
      <span>Tour Bookings<br>0400 118 206</span>
    </div>
    <div class="search"><span>Search entire site here</span>
      <svg width="14" height="14" viewBox="0 0 24 24"><circle cx="10" cy="10" r="6" fill="none" stroke="#999" stroke-width="2.5"/><path d="M15 15l6 6" stroke="#999" stroke-width="2.5"/></svg>
    </div>
    <div class="login"><svg width="13" height="13" viewBox="0 0 24 24"><path d="M3 12h12M11 7l5 5-5 5M15 3h6v18h-6" fill="none" stroke="#555" stroke-width="2.5"/></svg>Login</div>
  </header>

  <nav class="main-nav">
    <a>Home</a><a>Latest tours</a><a>Day + Night</a><a>Private functions</a><a>Locations</a><a>Stories</a><a>Bookings</a><a>Contact</a><a>Podcast</a><a>About us</a>
  </nav>

  <section class="hero" role="img" aria-label="Photograph of old red stone walls and round towers under a blue sky">
    <form class="booking-panel">
      <div class="step">
        <h3><b>01</b> What?</h3>
        <div class="options">
          <span class="opt"><span class="radio on"></span>Day Tour</span>
          <span class="opt"><span class="radio"></span>Night Tour</span>
          <span class="opt"><span class="radio"></span>Group Tour</span>
          <span class="opt"><span class="radio"></span>Private Event</span>
          <span class="opt"><span class="radio"></span>Story Walk</span>
          <span class="opt"><span class="radio"></span>Gift Voucher</span>
        </div>
      </div>
      <div class="step">
        <h3><b>02</b> Where?</h3>
        <div class="label">Your city</div>
        <div class="field">City, district or meeting point</div>
      </div>
      <div class="step">
        <h3><b>03</b> When?</h3>
        <div class="pair two">
          <div><div class="label">Tour date</div><div class="field"></div></div>
          <div><div class="label">Start time</div><div class="field"></div></div>
        </div>
      </div>
      <div class="step">
        <h3><b>04</b> Who?</h3>
        <div class="pair three">
          <div><div class="label">Adults</div><div class="field"></div></div>
          <div><div class="label">Seniors</div><div class="field"></div></div>
          <div><div class="label">Teens</div><div class="field"></div></div>
        </div>
      </div>
      <span class="proceed">Find your tour</span>
    </form>
  </section>

  <section class="offers">
    <h2>Explore our latest tours</h2>
    <div class="offer-grid">
      <div class="offer o1" role="img" aria-label="Photograph of an ornate old sandstone facade"></div>
      <div class="offer o2" role="img" aria-label="Photograph of weathered red city walls"></div>
      <div class="offer o3" role="img" aria-label="Photograph of a carved stone monument"></div>
      <div class="offer o4" role="img" aria-label="Photograph of an old fortress gate"></div>
    </div>
  </section>
</div>
</body>
</html>
```